Video Company website for high tech video software company

Design a website for a software company that has an extensive list of products that process incoming TV video and video ads and processes the video for delivery to mobile phones, tablets, Set Top Boxes, and PCs.

Coded - Design and coding required

1 page

```html
<!DOCTYPE html>
<html lang="en">
<head>
<meta charset="utf-8">
<title>Relayvision – High Quality Transcoding</title>
<link href="https://fonts.googleapis.com/css2?family=Rajdhani:wght@500;600;700&family=Poppins:wght@400;500&family=Roboto:wght@500;700&display=swap" rel="stylesheet">
<style>
  :root {
    --navy: #0b2150;
    --navy-deep: #071838;
    --ink: #222;
    --white: #fff;
    --accent: #2e54a4;
    --footer: #5ba3e0;
    --beam: #3d7bff;
    --card-shadow: rgba(0,0,0,0.18);
  }
  * { margin: 0; padding: 0; box-sizing: border-box; }
  html, body { width: 766px; height: 1200px; overflow: hidden; background: var(--white); }
  body { position: relative; font-family: 'Poppins', sans-serif; color: var(--ink); }

  .site-header { position: absolute; top: 0; left: 0; width: 766px; height: 52px; background: var(--white); }
  .brand { position: absolute; left: 71px; top: 18px; font-family: 'Roboto', sans-serif; font-weight: 700; font-size: 17px; color: #4a4f57; letter-spacing: -0.3px; }
  .main-nav { position: absolute; top: 28px; left: 0; width: 766px; font-family: 'Roboto', sans-serif; font-weight: 500; font-size: 8.2px; color: var(--ink); }
  .main-nav a { position: absolute; white-space: nowrap; color: inherit; text-decoration: none; }

  .hero { position: absolute; top: 52px; left: 0; width: 766px; height: 383px; overflow: hidden;
    background: radial-gradient(ellipse at 55% 40%, #143170 0%, var(--navy) 55%, var(--navy-deep) 100%); }
  .hero-title { position: absolute; left: 0; width: 780px; top: 36px; text-align: center; font-family: 'Rajdhani', sans-serif; font-weight: 700; font-size: 50px; line-height: 57px; color: var(--white); }
  .dish-art { position: absolute; left: 0; top: 134px; width: 232px; height: 249px;
    background: linear-gradient(160deg, rgba(255,255,255,0.92), rgba(220,230,245,0.75)); border-radius: 0 60% 10% 0; }
  .devices-art { position: absolute; left: 572px; top: 34px; width: 194px; height: 322px;
    background: radial-gradient(ellipse at 55% 50%, rgba(160,185,230,0.28), rgba(11,33,80,0) 70%); }
  .pipeline { position: absolute; left: 0; top: 0; }
  .stage { position: absolute; font-family: 'Roboto', sans-serif; font-weight: 700; font-size: 6.4px; line-height: 12px; color: var(--white); text-align: center; white-space: nowrap; transform: translateX(-50%); }

  .services-title { position: absolute; top: 482px; width: 766px; text-align: center; font-family: 'Rajdhani', sans-serif; font-weight: 700; font-size: 28px; color: var(--ink); }
  .service-card { position: absolute; width: 192px; height: 231px; background: var(--white); border-radius: 4px; box-shadow: 0 1px 5px var(--card-shadow); overflow: hidden; }
  .service-photo { height: 138px; }
  .service-text { height: 93px; display: flex; align-items: center; justify-content: center; padding: 0 12px; text-align: center; font-size: 10px; line-height: 17px; color: var(--ink); }

  .btn-more { position: absolute; left: 288px; top: 1047px; width: 190px; height: 44px; border-radius: 4px; background: var(--accent); color: var(--white); font-family: 'Rajdhani', sans-serif; font-weight: 700; font-size: 13px; display: flex; align-items: center; justify-content: center; text-decoration: none; }

  .site-footer { position: absolute; left: 0; top: 1145px; width: 766px; height: 55px; background: var(--footer); color: var(--white); font-size: 10px; display: flex; align-items: center; justify-content: center; }
</style>
</head>
<body>
  <header class="site-header">
    <div class="brand">Relayvision</div>
    <nav class="main-nav">
      <a style="left:207px">HOME</a>
      <a style="left:247px">CAS</a>
      <a style="left:280px">MULTI SCREEN DRM</a>
      <a style="left:379px">COST OF OWNERSHIP</a>
      <a style="left:481px">RENEWAL</a>
      <a style="left:538px">RELIABILITY</a>
      <a style="left:604px">TEAM</a>
      <a style="left:643px">CONTACT US</a>
    </nav>
  </header>

  <section class="hero">
    <div class="dish-art" role="img" aria-label="Line illustration of a satellite dish"></div>
    <div class="devices-art" role="img" aria-label="Phones and tablets receiving the video stream"></div>
    <h1 class="hero-title">High Quality<br>Transcoding</h1>

    <svg class="pipeline" width="766" height="383" viewBox="0 0 766 383">
      <line x1="159" y1="213" x2="585" y2="213" stroke="var(--beam)" stroke-width="3"/>
      <line x1="159" y1="213" x2="585" y2="213" stroke="#cfe0ff" stroke-width="1"/>
      <g stroke="#fff" stroke-width="0.8">
        <line x1="254" y1="197" x2="254" y2="228"/>
        <line x1="321" y1="197" x2="321" y2="228"/>
        <line x1="384" y1="197" x2="384" y2="228"/>
        <line x1="443" y1="197" x2="443" y2="228"/>
        <line x1="497" y1="197" x2="497" y2="228"/>
        <line x1="530" y1="197" x2="530" y2="228"/>
        <line x1="555" y1="197" x2="555" y2="228"/>
      </g>
      <g fill="#fff">
        <rect x="228" y="240" width="8" height="6" rx="1"/>
        <rect x="240" y="240" width="9" height="6" rx="1"/>
        <rect x="254" y="240" width="9" height="6" rx="1" fill="#e6b400"/>
        <rect x="265" y="240" width="10" height="6" rx="1" fill="#e6b400"/>
      </g>
    </svg>

    <div class="stage" style="left:254px;top:168px">Ingest<br>Transcoding</div>
    <div class="stage" style="left:320px;top:168px">Middleware</div>
    <div class="stage" style="left:384px;top:168px">Subscriber<br>Management</div>
    <div class="stage" style="left:441px;top:168px">Security</div>
    <div class="stage" style="left:495px;top:168px">Streaming</div>
    <div class="stage" style="left:531px;top:168px">Ads</div>
    <div class="stage" style="left:556px;top:168px">Apps</div>

    <div class="stage" style="left:321px;top:239px">EPG cms<br>catchup tv</div>
    <div class="stage" style="left:389px;top:239px">Billing packages<br>payments</div>
    <div class="stage" style="left:448px;top:239px">Approved cas</div>
    <div class="stage" style="left:501px;top:239px">1,000,000+<br>streams<br>edge cache</div>
    <div class="stage" style="left:557px;top:239px">Targeted<br>Region<br>Genre</div>
  </section>

  <h2 class="services-title">Our Services</h2>

  <article class="service-card" style="left:71px;top:541px">
    <div class="service-photo" role="img" aria-label="Person relaxing on a sofa watching television" style="background:linear-gradient(160deg,#d9d6d2,#8a8f74 55%,#6d5a4b)"></div>
    <p class="service-text">OTT / IPTV Apps Live Tv Catchup Tv VOD Recommendations</p>
  </article>
  <article class="service-card" style="left:287px;top:541px">
    <div class="service-photo" role="img" aria-label="Hand touching a glowing network globe" style="background:linear-gradient(160deg,#8e98a3,#4f5963 60%,#2d343b)"></div>
    <p class="service-text">MSO Scale Clould Option NationalwideDistribution Individual Lineups Shared Infrastructure</p>
  </article>
  <article class="service-card" style="left:503px;top:541px">
    <div class="service-photo" role="img" aria-label="Viewer browsing a wall of streaming titles" style="background:linear-gradient(160deg,#2d4f6e,#1c2c3e 55%,#b48a4a)"></div>
    <p class="service-text">Advertising Targeted Advertising Regional Addressable ads ad analystics</p>
  </article>

  <article class="service-card" style="left:71px;top:788px">
    <div class="service-photo" role="img" aria-label="Hand over a smartphone with glowing data stream" style="background:linear-gradient(160deg,#2a5e95,#13345c 55%,#0a1a30)"></div>
    <p class="service-text">CAS / DRM Hollywood approved Highly secure CAS and DRM Systems</p>
  </article>
  <article class="service-card" style="left:287px;top:788px">
    <div class="service-photo" role="img" aria-label="Man on a sofa browsing films on a tablet" style="background:linear-gradient(160deg,#6e6a66,#9a7a52 55%,#2f3a52)"></div>
    <p class="service-text">High Capacity Streaming Edge Cache Cloud managed No 3rd Party CDN needed</p>
  </article>
  <article class="service-card" style="left:503px;top:788px">
    <div class="service-photo" role="img" aria-label="Tablet showing a live sports stream" style="background:linear-gradient(160deg,#5c5c5c,#c79a4a 55%,#2a2a2a)"></div>
    <p class="service-text" style="padding:0 36px">Subscriber Management System</p>
  </article>

  <a class="btn-more" href="#">View More Services</a>

  <footer class="site-footer">© 2021 All Rights Reserved</footer>
</body>
</html>
```